Design website banners for teeth whitening clinic based on clear examples we have provided.

Hi All,

Thank for for looking at my design project. I am looking forward to seeing your work and providing some feedback.

We are a teeth whitening company called Gleamora Dental and we are having our website updated as we speak. For the new site we are in need of several banners

I have attached some banners which we love and we would love to keep the same style/theme for our banners.

We like the blue fading squares from the edges of the banners so we would like to keep this as a consistent theme across all banners.

HOMEPAGE BANNERS to be the following dimensions: 1920 width x 800 height

Banner1.1 ( Varnek More Info):
Headline Text: Worlds most advanced, award winning whitening technology
Button: Read More
Image: please use picture of Trelwin Varnek whitening machine
Background: Please use photo of someone smiling - white teeth

Banner 1.2 (Varnek Book Now - same as banner 1.1 but with different button) :
Button: Book Now

Banner2.1 (Varnek special1) :
Headline Text: Worlds most advanced whitening technology just got better.
Headline subtext: 1-Hour In chair treatment for just $149! Save $350 -
Button: Book Now
Background: Please use photo of someone smiling - white teeth ( can be same as banner 1)

Banner2.2 (Varnek special2 - same as banner 2.1 just with different price) :
Headline subtext: 1-Hour In chair treatment for just $129! Save $370 -
Button: Book Now

Banner3 ( Whitening pens) :
Headline Text: Any time, any where.
Button: Buy Now
Image: please use images of gleamora dental teeth whitening pens
( Same look, feel and layout to the image attached called Pens Example)
Background: Please use photo of someone smiling - white teeth - can be a couple or anything. Just use judgement what you think looks good.

Banner4 ( Whitening Kits) :
Headline Text: The revolution in home teeth whitening is here
Button: Buy Now
Image: Product images arent ready yet but please leave space for them to be put in later.

SPECIFIC PAGE BANNERS - These do not need images of the actual product in them. These need to be 1600 x 500 size

Banner5 ( Online Store) :
Headline Text: Online Store
Headline Sub text: 48 Hour Express Delivery Nationwide
Background: Just use judgement what you think looks good.

Banner6 ( Whitening Kits ) :
Headline Text: At Home teeth whitening system
(Please see image attached called ' home whitening system' and use this as an example)

Banner7 ( Whitening Pens ) :

There will be 2 more to come.

Target Market(s)

Mostly (70%) Female customers between 20-40 years old who take pride in their personal appearance and dont mind spending money on cosmetic enhancements.

Industry/Entity Type

Clinic

Requirements
Must have
• A very similar look and feel to the banner examples provided and those that can be seen on www.lumidexa.com
• Colour should fit in with logo of www.gleamoradental.co.nz eg: light- medium blue

```html
<!DOCTYPE html>
<html lang="en">
<head>
<meta charset="utf-8">
<title>Gleamora Dental — Page Banners</title>
<link rel="stylesheet" href="https://fonts.googleapis.com/css2?family=Open+Sans:wght@300;400;600&display=swap">
<style>
  :root {
    --backdrop: #939498;
    --panel: #f4f1f1;
    --ink: #636363;
    --accent: #47bff2;
    --on-accent: #ffffff;
  }
  html, body {
    margin: 0;
    padding: 0;
    width: 1200px;
    height: 1000px;
    overflow: hidden;
    background: var(--backdrop);
    font-family: "Open Sans", Arial, sans-serif;
  }
  .canvas {
    position: relative;
    width: 1200px;
    height: 1000px;
  }
  .banner {
    position: absolute;
    left: 15px;
    width: 1168px;
    background: var(--panel);
    text-align: center;
  }
  .banner--store {
    top: 109px;
    height: 364px;
  }
  .banner--home-kit {
    top: 488px;
    height: 363px;
  }
  .store-title {
    position: absolute;
    left: 0;
    right: 0;
    top: 60px;
    margin: 0;
    font-weight: 300;
    font-size: 116px;
    line-height: 116px;
    color: var(--ink);
    letter-spacing: 0.5px;
  }
  .delivery-band {
    position: absolute;
    left: 0;
    right: 0;
    top: 203px;
    height: 100px;
    margin: 0;
    background: var(--accent);
    color: var(--on-accent);
    font-weight: 600;
    font-size: 49px;
    line-height: 100px;
    white-space: nowrap;
  }
  .kit-title {
    position: absolute;
    left: 0;
    right: 0;
    top: 56px;
    margin: 0;
    font-weight: 300;
    font-size: 102px;
    line-height: 112px;
    color: var(--ink);
    white-space: nowrap;
  }
  .kit-title .highlight {
    display: block;
    color: var(--accent);
  }
</style>
</head>
<body>
<main class="canvas">
  <section class="banner banner--store">
    <h1 class="store-title">Online Store</h1>
    <p class="delivery-band">48 Hour Express Delivery Nationwide</p>
  </section>
  <section class="banner banner--home-kit">
    <h2 class="kit-title"><span class="highlight">At Home teeth</span>whitening system</h2>
  </section>
</main>
</body>
</html>
```